Webdesign für Immobilienmakler / Immobilienbüro
Zielgruppe
Das Unternehmen heißt LUMAR GmbH und kommt aus Heerbrugg in der Schweiz und will nun den Bereich Immobilien Vermarktung, Verkauf, Vermietung auf Süddeutschland erweitern.
Wir haben bis heute keine Webseite, weil unser Geschäft bis dato in der Schweiz durch Empfehlung, Mundpropaganda und Zeitunganzeigen funktioniert hat. Aber in Deutschland ist es ja ein Muß, was uns sicherlich auch den Einstieg erleichtern wird.
Aufgabenstellung
Wir benötigen eine Homepage für den Verkauf, Vermietung, Vermittlung von Immobilien für Privat und Gewerbe. Zu den Kategorien und der Gliederung haben wir keine bestimmte Vorstellung.
Hier hat der Designer freie Hand und wir freuen uns auf Ihren Vorschlag

```html
<!DOCTYPE html>
<html lang="de">
<head>
<meta charset="utf-8">
<title>Lumar GmbH – Immobilien</title>
<link href="https://fonts.googleapis.com/css2?family=Crimson+Text:ital,wght@0,400;0,600&family=Arimo:ital,wght@0,400;1,400&display=swap" rel="stylesheet">
<style>
:root{
  --cream:#ecead8;
  --cream-top:#e3e0c9;
  --cream-band:#e5e1ca;
  --card:#dcd7bf;
  --red:#640000;
  --red-dark:#4e0000;
  --red-deep:#3a0c05;
  --ink:#2e2e2e;
  --text:#333;
  --muted:#777;
  --link:#8c1a12;
  --serif:"Crimson Text", Georgia, serif;
  --sans:"Arimo", Arial, sans-serif;
}
html,body{margin:0;width:929px;height:1200px;overflow:hidden;background:var(--cream)}
.page{position:relative;width:1200px;height:1550px;transform:scale(.77417);transform-origin:0 0;background:var(--cream);font-family:var(--sans);color:var(--text);overflow:hidden}
.abs{position:absolute}
.top-band{left:0;top:0;width:1200px;height:370px;background:var(--cream-top)}
.contact-note{left:152px;top:19px;font-size:10px;color:var(--muted)}
.contact-phone{left:152px;top:33px;font-size:14px;color:#666}
.social{right:150px;top:28px;display:flex;gap:18px}
.social span{width:22px;height:22px;border-radius:50%;background:#b9b7a8}
.social svg{display:block}

.nav-tab{top:89px;width:53px;height:68px;background:var(--red)}
.nav-bar{left:138px;top:75px;width:924px;height:67px;background:var(--red)}
.nav{top:75px;height:67px;display:flex;font-family:var(--serif);font-size:20px;color:#fff}
.nav a{display:flex;align-items:center;padding:0 20px;color:#fff;text-decoration:none}
.nav a.active{background:var(--red-deep)}
.nav-left{left:152px}
.nav-right{right:150px}

.logo{left:515px;top:0;width:170px;height:207px}
.logo-text{left:515px;top:62px;width:170px;text-align:center;color:#fff;font-family:var(--serif);line-height:1}
.logo-text .name{font-size:30px;display:block}
.logo-text .form{font-size:20px;display:block;margin-top:4px}

.hero{left:150px;top:142px;width:900px;height:364px;background:linear-gradient(180deg,#3d5a2a 0%,#8b8a78 35%,#b9b2a0 60%,#5d7a2f 85%,#6c8f2e 100%)}
.hero-caption{left:700px;top:383px;width:290px;height:101px;background:rgba(30,25,20,.6);color:#fff}
.hero-caption h2{margin:8px 0 0 16px;font:400 30px var(--serif)}
.hero-caption p{margin:2px 16px 0 16px;font-size:13px;line-height:16px}
.arrow{width:62px;height:52px;background:var(--red);display:flex;align-items:center;justify-content:center}
.arrow-fold{width:0;height:0;border-style:solid}

.search{left:150px;top:506px;width:900px;height:55px;background:var(--red)}
.search-label{left:161px;top:518px;font:400 21px var(--serif);color:#fff}
.field{height:27px;border:1px solid #d9c9c0;background:var(--red-deep);box-sizing:border-box;top:519px;color:#eee;font:11px var(--serif);padding:6px 9px}
.field-label{top:527px;font:11px var(--serif);color:#eee}
.btn-search{left:927px;top:519px;width:111px;height:28px;border:1px solid #d9c9c0;box-sizing:border-box;color:#fff;font:11px var(--serif);text-align:center;line-height:26px}

.section-title{left:150px;top:604px;width:899px;display:flex;align-items:center;gap:14px;font:400 30px var(--serif);color:var(--ink)}
.section-title::before,.section-title::after{content:"";flex:1;height:1px;background:#444;margin-top:14px}

.card{top:686px;width:251px;height:295px;background:var(--card)}
.card-photo{height:150px}
.card p{margin:0;padding:0 8px;font-size:13px;line-height:15.7px;color:#333}
.card .more{position:absolute;right:0;bottom:0;width:120px;height:30px;background:var(--red);color:#fff;font-size:13px;text-align:center;line-height:30px}

.lower{left:0;top:1052px;width:1200px;height:425px;background:var(--cream-band)}
.col-title{font:400 29px var(--serif);color:var(--ink);border-bottom:1px solid #333;padding-bottom:2px}
.about p{margin:0 0 16px;font-size:13px;line-height:15.6px}
.about a{color:var(--link);text-decoration:none}
.news-item{left:704px;width:367px}
.badge{position:absolute;left:0;top:0;width:45px;height:55px}
.badge-text{position:absolute;left:0;top:3px;width:45px;text-align:center;color:#fff;line-height:1}
.badge-text b{display:block;font-size:15px}
.badge-text small{font-size:11px}
.news-item p{margin:0 0 0 57px;width:300px;font-size:13px;line-height:15.7px}
.news-more{text-align:right;font-style:italic;font-size:13px;color:var(--red-dark);margin-top:6px}
.news-all{left:880px;top:1420px;width:179px;text-align:right;font-style:italic;font-size:13px;color:var(--red-dark)}

.footer{left:0;top:1477px;width:1200px;height:73px;background:var(--red-dark)}
.footer-brand{left:141px;top:1495px;color:#fff;font:400 21px var(--serif)}
.footer-brand small{font:13px var(--sans);margin-left:8px}
.footer-nav{right:139px;top:1500px;display:flex;gap:24px;font:13px var(--serif);color:#fff}
</style>
</head>
<body>
<div class="page">
  <div class="abs top-band"></div>

  <div class="abs contact-note">Bei Fragen stehen wir Ihnen gerne zur Seite</div>
  <div class="abs contact-phone">+01234 765 31980</div>
  <div class="abs social" aria-label="Soziale Netzwerke">
    <span></span><span></span><span></span>
    <svg width="22" height="16" viewBox="0 0 22 16" aria-label="E-Mail"><rect x="1" y="1" width="20" height="14" fill="none" stroke="#b9b7a8" stroke-width="2"/><path d="M1 1 L11 9 L21 1" fill="none" stroke="#b9b7a8" stroke-width="2"/></svg>
  </div>

  <div class="abs nav-tab" style="left:97px"></div>
  <div class="abs nav-tab" style="left:1051px"></div>
  <div class="abs nav-bar"></div>
  <nav class="abs nav nav-left">
    <a class="active">Startseite</a><a>Immobilien</a><a>Service</a>
  </nav>
  <nav class="abs nav nav-right">
    <a>Über Lumar</a><a>Pachten</a><a>Kontakt</a>
  </nav>

  <div class="abs hero" role="img" aria-label="Foto: modernes Holzhaus mit Rasen zwischen hohen Bäumen"></div>
  <div class="abs hero-caption">
    <h2>Lorem</h2>
    <p>Duis autem vel eum iriure dolor in hendrerit in vulputate velit esse molestie consequat.</p>
  </div>

  <svg class="abs logo" viewBox="0 0 170 207">
    <defs><linearGradient id="rib" x1="0" y1="0" x2="0" y2="1"><stop offset="0" stop-color="#4a0000"/><stop offset="1" stop-color="#6a0202"/></linearGradient></defs>
    <polygon points="0,0 170,0 170,207 85,145 0,207" fill="url(#rib)"/>
  </svg>
  <div class="abs logo-text"><span class="name">Lumar</span><span class="form">GmbH</span></div>

  <div class="abs arrow" style="left:127px;top:341px">
    <svg width="16" height="24" viewBox="0 0 16 24"><path d="M12 2 L3 12 L12 22" fill="none" stroke="#fff" stroke-width="2"/></svg>
  </div>
  <div class="abs arrow-fold" style="left:127px;top:393px;border-width:0 23px 14px 0;border-color:transparent #3a0000 transparent transparent"></div>
  <div class="abs arrow" style="left:1010px;top:333px">
    <svg width="16" height="24" viewBox="0 0 16 24"><path d="M4 2 L13 12 L4 22" fill="none" stroke="#fff" stroke-width="2"/></svg>
  </div>
  <div class="abs arrow-fold" style="left:1050px;top:385px;border-width:0 0 14px 22px;border-color:transparent transparent transparent #3a0000"></div>

  <div class="abs search"></div>
  <div class="abs search-label">Immobiliensuche</div>
  <div class="abs field" style="left:305px;width:141px">Ort, Plz oder Stadtteil</div>
  <div class="abs field" style="left:461px;width:116px">Mietwohnung
    <svg style="position:absolute;right:6px;top:8px" width="12" height="10" viewBox="0 0 12 10"><polygon points="0,0 12,0 6,10" fill="#fff"/></svg>
  </div>
  <div class="abs field-label" style="left:587px">Preis(€)</div>
  <div class="abs field" style="left:627px;width:52px"></div>
  <div class="abs field-label" style="left:693px">Größe(m²)</div>
  <div class="abs field" style="left:749px;width:52px"></div>
  <div class="abs field-label" style="left:808px">Zimmer</div>
  <div class="abs field" style="left:852px;width:52px"></div>
  <div class="abs btn-search">Suche starten</div>

  <h2 class="abs section-title" style="margin:0">Lorem ipsum</h2>

  <article class="abs card" style="left:150px">
    <div class="card-photo" role="img" aria-label="Foto: helles Holzhaus hinter Bäumen" style="background:linear-gradient(180deg,#4e6e2c,#c8c4b2 55%,#5f8a2a)"></div>
    <p style="margin-top:19px">Lorem ipsum dolor sit amet, consetetur sadipscing elitr, sed diam nonumy eirmod tempor invidunt ut labore et dolore magna aliquyam erat, sed diam voluptua.</p>
    <div class="more">mehr Erfahren</div>
  </article>
  <article class="abs card" style="left:475px">
    <div class="card-photo" role="img" aria-label="Foto: altes Haus mit blauer Fassade im Grünen" style="background:linear-gradient(180deg,#c9d0c6,#6c9ab4 40%,#5b4a3a 65%,#4f6b34)"></div>
    <p style="margin-top:34px">Lorem ipsum dolor sit amet, consetetur sadipscing elitr, sed diam nonumy eirmod tempor invidunt ut labore et dolore magna aliquyam erat, sed diam voluptua.</p>
    <div class="more">mehr Erfahren</div>
  </article>
  <article class="abs card" style="left:800px">
    <div class="card-photo" role="img" aria-label="Foto: zweistöckiges Wohnhaus mit heller Fassade" style="background:linear-gradient(180deg,#e8e6e2,#d8c9a0 40%,#c9b98f 75%,#6d7a4a)"></div>
    <p style="margin-top:34px">Lorem ipsum dolor sit amet, consetetur sadipscing elitr, sed diam nonumy eirmod tempor invidunt ut labore et dolore magna aliquyam erat, sed diam voluptua.</p>
    <div class="more">mehr Erfahren</div>
  </article>

  <div class="abs lower"></div>

  <section class="abs about" style="left:138px;top:1066px;width:496px">
    <div class="col-title">Wir über uns</div>
    <div style="padding:20px 2px 0">
      <p>Ut wisi enim ad minim veniam, quis <a>nostrud</a> exerci tation ullamcorper suscipit lobortis nisl ut aliquip ex ea commodo consequat. Duis autem vel eum iriure dolor in hendrerit in vulputate velit esse molestie consequat, vel illum dolore eu feugiat nulla facilisis at vero eros et accumsan et iusto odio dignissim qui <a>blandit</a> praesent luptatum zzril delenit augue duis dolore te feugait nulla facilisi.</p>
      <p>Nam liber tempor cum soluta nobis eleifend option congue nihil imperdiet doming id quod mazim placerat facer possim assum. Lorem ipsum dolor sit amet, consectetuer adipiscing elit, sed diam nonummy nibh <a>euismod</a> tincidunt ut laoreet dolore magna aliquam erat volutpat. Ut wisi enim ad minim veniam, quis nostrud exerci tation ullamcorper suscipit lobortis nisl ut aliquip ex ea commodo consequat.</p>
    </div>
  </section>

  <section class="abs" style="left:704px;top:1069px;width:359px">
    <div class="col-title">Neuigkeiten</div>
  </section>

  <div class="abs news-item" style="top:1131px">
    <svg class="badge" viewBox="0 0 45 55"><polygon points="0,0 45,0 45,55 22.5,42 0,55" fill="var(--red)"/></svg>
    <div class="badge-text"><b>08</b><small>NOV</small></div>
    <p>Ut wisi enim ad minim veniam, quis nostrud exerci tation ullamcorper suscipit lobortis nisl ut aliquip ex ea commodo consequat. Duis autem vel eum iriure dolor in hendrerit in vulputate velit esse molestie consequat, vel illum dolore eu feugiat nulla facilisis at vero eros et</p>
    <div class="news-more">mehr erfahren</div>
  </div>
  <div class="abs news-item" style="top:1272px">
    <svg class="badge" viewBox="0 0 45 55"><polygon points="0,0 45,0 45,55 22.5,42 0,55" fill="var(--red)"/></svg>
    <div class="badge-text"><b>24</b><small>OKT</small></div>
    <p>Ut wisi enim ad minim veniam, quis nostrud exerci tation ullamcorper suscipit lobortis nisl ut aliquip ex ea commodo consequat. Duis autem vel eum iriure dolor in hendrerit in vulputate velit esse molestie consequat, vel illum dolore eu feugiat nulla facilisis at vero eros et</p>
    <div class="news-more">mehr erfahren</div>
  </div>
  <div class="abs news-all">weitere Neuigkeiten</div>

  <footer class="abs footer"></footer>
  <div class="abs footer-brand">Lumar GmbH<small>© 2013</small></div>
  <nav class="abs footer-nav">
    <span>Startseite</span><span>Immobilien</span><span>Service</span><span>Über Lumar</span><span>Pachten</span><span>Kontakt</span>
  </nav>
</div>
</body>
</html>
```